food label design

we need a label design for honey, we are beekeepers in WA/ Western Australia we produce many type of honey, so the label should suit all types. either by changing the name or colour variation etc, There is many great designs we have seen on google. But the design we had was not satisfying, maybe because we have seen many good ones that the design didn't impress us. We would like something that can be called premium and also unique
Updates

Target Market(s)

food, honey

Logo Text

amber wren

Font styles to use
Serif
Sans Serif
Decorative
Script

Colors

Designer to choose colors to be used in the design.

Requirements
Nice to have
• since the package already includes the logo design, could you guys just add the new logo design into the label? since that would make my selection of the winning project easier.
• the original logo, it did look nice but im not sure if its ok to have amber premium wren in the logo so yea. looking forward to see some new and better designs.
• Also it would be nice if designers can include the sizes of the label, or just some suggestion that could make it look better. since the size will affect like the word font etc bottle have different sizes.
• Also if can show the design on a honey bottle will be nice, we currently use hexagon bottle would consider cylinder in the future so if the design can include these would be perfect.
Should not have
• the attachment i included is the label design i have at the moment, it is nice but im not very impressed with it. Since one of the beekeepers in my State use almost the same design just different colour

```html
<!DOCTYPE html>
<html lang="en">
<head>
<meta charset="utf-8">
<title>Amber Wren – Clover Flavour Honey Label</title>
<link href="https://fonts.googleapis.com/css2?family=Oswald:wght@500;600&family=Open+Sans:wght@400;600&family=PT+Sans:wght@400;700&display=swap" rel="stylesheet">
<style>
  :root {
    --backdrop: #e2e2e2;
    --label-orange: #f6a42f;
    --comb-light: #f9b95a;
    --comb-faint: #f8ae45;
    --ink: #1c1206;
    --ink-soft: #2b1d0b;
    --cream: #fff7e8;
  }
  * { margin: 0; padding: 0; box-sizing: border-box; }
  html, body { width: 1200px; height: 849px; overflow: hidden; }
  body { background: var(--backdrop); position: relative; font-family: "Open Sans", sans-serif; color: var(--ink); }

  .label-panel {
    position: absolute; top: 296px; width: 332px; height: 256px;
    background: var(--label-orange); overflow: hidden;
  }
  .label-panel--nutrition { left: 84px; }
  .label-panel--front { left: 434px; }
  .label-panel--story { left: 784px; }

  .comb-pattern { position: absolute; }
  .label-panel--nutrition .comb-pattern {
    right: 0; top: 0; width: 112px; height: 256px;
    background: linear-gradient(90deg, var(--label-orange), var(--comb-light) 55%, var(--comb-faint));
  }
  .label-panel--front .comb-pattern {
    left: 44px; top: 0; width: 236px; height: 184px;
    background: radial-gradient(ellipse at center, var(--comb-light) 0%, var(--comb-faint) 55%, var(--label-orange) 100%);
  }
  .label-panel--story .comb-pattern {
    left: 0; top: 70px; width: 70px; height: 186px;
    background: linear-gradient(0deg, var(--comb-light), var(--label-orange));
  }

  /* Nutrition side */
  .nutrition { position: absolute; inset: 0; font-family: "PT Sans", sans-serif; text-transform: uppercase; }
  .infant-warning { position: absolute; left: 42px; top: 32px; font-size: 10px; letter-spacing: -0.1px; }
  .nutrition-head { position: absolute; left: 66px; font-size: 5px; font-weight: 700; }
  .nutrition-title { top: 54px; }
  .net-weight { position: absolute; left: 200px; top: 54px; font-size: 5px; font-weight: 700; }
  .col-head { top: 74px; }
  .col-head span { position: absolute; white-space: nowrap; }
  .nutrition-table { position: absolute; left: 64px; top: 92px; border-collapse: collapse; font-size: 8px; }
  .nutrition-table td { height: 10px; line-height: 10px; padding: 0; }
  .nutrition-table td:nth-child(1) { width: 108px; }
  .nutrition-table td:nth-child(2) { width: 48px; text-transform: none; }
  .nutrition-table td:nth-child(3) { text-transform: none; }
  .storage { position: absolute; left: 0; width: 260px; top: 198px; text-align: center; font-size: 9px; line-height: 12px; text-transform: none; font-family: "Open Sans", sans-serif; }
  .pack-weight { position: absolute; left: 0; width: 260px; top: 234px; text-align: center; font-size: 10px; text-transform: none; font-family: "Open Sans", sans-serif; }

  /* Front */
  .brand-mark { position: absolute; left: 0; right: 0; top: 88px; display: flex; justify-content: center; align-items: center; gap: 8px; }
  .brand-dot { width: 12px; height: 12px; border-radius: 50%; background: var(--cream); }
  .brand-name { font-family: "Oswald", sans-serif; font-weight: 600; font-size: 26px; letter-spacing: 1px; color: var(--ink); text-transform: uppercase; }
  .flavour-name { position: absolute; left: 0; right: 0; top: 196px; text-align: center; font-family: "Oswald", sans-serif; font-weight: 600; font-size: 23px; line-height: 28px; color: var(--ink); text-transform: uppercase; letter-spacing: 0.2px; }
  .honey-origin { position: absolute; left: 0; right: 0; top: 229px; text-align: center; font-family: "Open Sans", sans-serif; font-weight: 600; font-size: 7px; letter-spacing: 1.4px; text-transform: uppercase; }

  /* Story side */
  .story { position: absolute; inset: 0; font-size: 8px; line-height: 10px; color: var(--ink-soft); }
  .story p { position: absolute; left: 44px; width: 262px; }
  .story-intro { top: 34px; }
  .story-intro strong { font-size: 11.5px; font-weight: 400; margin-right: 10px; }
  .story-body { top: 74px; }
  .story-claim { top: 124px; left: 78px !important; font-size: 10px; }
  .story-producer { top: 154px; font-size: 8.5px; }
  .story-contact { top: 176px; line-height: 11px; }
</style>
</head>
<body>

<section class="label-panel label-panel--nutrition" aria-label="Nutrition side of label">
  <div class="comb-pattern" role="img" aria-label="Faint honeycomb hexagon pattern"></div>
  <div class="nutrition">
    <p class="infant-warning">Do not give to infants under 12 months old</p>
    <p class="nutrition-head nutrition-title">Nutrition information</p>
    <p class="net-weight">Net weight 250g</p>
    <p class="nutrition-head col-head">
      <span style="left:0">Servings per pack approx 17</span>
      <span style="left:96px">Per serving</span>
      <span style="left:150px">Per 100g</span>
    </p>
    <table class="nutrition-table">
      <tr><td>Energy</td><td>210kJ</td><td>1400kJ</td></tr>
      <tr><td>Protein</td><td>0.0g</td><td>0.3g</td></tr>
      <tr><td>Fat, total</td><td>0.0g</td><td>0.0g</td></tr>
      <tr><td>Carbohydrate</td><td>12.3g</td><td>82.1g</td></tr>
      <tr><td>Sugars</td><td>12.3g</td><td>82.1g</td></tr>
      <tr><td>Sodium</td><td>2mg</td><td>14mg</td></tr>
      <tr><td>Ash residue</td><td>0.1g</td><td>0.3g</td></tr>
      <tr><td>Moisture</td><td>0.1g</td><td>0.3g</td></tr>
    </table>
    <p class="storage">Store at room temperature<br>Do not Microwave/Refrigerate</p>
    <p class="pack-weight">250g</p>
  </div>
</section>

<section class="label-panel label-panel--front" aria-label="Front of label">
  <div class="comb-pattern" role="img" aria-label="Honeycomb hexagon pattern behind the brand"></div>
  <div class="brand-mark">
    <span class="brand-dot"></span>
    <span class="brand-name">Amber Wren</span>
  </div>
  <h1 class="flavour-name">Clover Flavour</h1>
  <p class="honey-origin">Raw Western Australian Honey</p>
</section>

<section class="label-panel label-panel--story" aria-label="Brand story side of label">
  <div class="comb-pattern" role="img" aria-label="Faint honeycomb hexagon pattern"></div>
  <div class="story">
    <p class="story-intro"><strong>Amber Wren</strong>passion in producing high quality honey to our customers</p>
    <p class="story-body">Our honey is all natural, unheated and unprocessed, from the nectar of our western australian flowers, to bees then to you.</p>
    <p class="story-claim">100% Natural Australian Honey</p>
    <p class="story-producer">Produced and packed by: AMBER WREN</p>
    <p class="story-contact">14 Marlow Crescent, Harbourvale WA 6190<br>0400123987<br>www.amberwren.com.au</p>
  </div>
</section>

</body>
</html>
```